International recycling company needs urgently logo and dossier cover design

We have a logo, but we need it valid to print (pdf, CMYK, 300dpi).
Attached you will find what we have.
Besides, we need a cover design for a corporate dossier, with the logo and corporate colours, nothing else.

Industry/Entity Type

Recycling

Colors
0492cd
32a6d7
85cae6
cde9f5

Requirements
Must have
• Flat color soft blue background.

```html
<!DOCTYPE html>
<html lang="en">
<head>
<meta charset="utf-8">
<title>OreLink – Dossier Cover</title>
<link rel="stylesheet" href="https://fonts.googleapis.com/css2?family=Cormorant+Garamond:wght@700&display=swap">
<style>
  :root {
    --blue-deep: #0492cd;
    --blue-mid: #32a6d7;
    --blue-light: #85cae6;
    --blue-pale: #cde9f5;
    --ink: #1a72b8;
    --stage: #8fa6a8;
  }
  html, body {
    margin: 0;
    padding: 0;
    width: 1200px;
    height: 1200px;
    overflow: hidden;
    background: var(--stage);
  }
  .canvas {
    position: relative;
    width: 1200px;
    height: 1200px;
  }
  .dossier-cover {
    position: absolute;
    left: 200px;
    top: 40px;
    width: 800px;
    height: 1120px;
    background: var(--blue-pale);
    overflow: hidden;
  }
  .cover-globe {
    position: absolute;
    left: 77px;
    top: 72px;
    width: 646px;
    height: 646px;
    border-radius: 50%;
    background: radial-gradient(circle at 40% 35%, var(--blue-mid), var(--blue-deep) 70%, #0a6fb0);
  }
  .brand {
    position: absolute;
    left: 0;
    width: 100%;
    text-align: center;
    font-family: "Cormorant Garamond", Georgia, serif;
    font-weight: 700;
    color: var(--ink);
    margin: 0;
  }
  .brand-name {
    top: 735px;
    font-size: 84px;
    line-height: 1;
  }
  .brand-tagline {
    top: 832px;
    font-size: 42px;
    line-height: 1;
  }
  .cover-wave {
    position: absolute;
    left: 0;
    top: 0;
    width: 800px;
    height: 1120px;
  }
</style>
</head>
<body>
<main class="canvas">
  <section class="dossier-cover">
    <div class="cover-globe" role="img" aria-label="Large blue globe showing the Americas"></div>
    <p class="brand brand-name">OreLink</p>
    <p class="brand brand-tagline">Ore Resources Company</p>
    <svg class="cover-wave" viewBox="0 0 800 1120" aria-hidden="true">
      <defs>
        <linearGradient id="waveFill" x1="0" y1="0" x2="0" y2="1">
          <stop offset="0" stop-color="#a9d9ee"/>
          <stop offset="1" stop-color="#6fbce0"/>
        </linearGradient>
        <linearGradient id="bandDeep" x1="0" y1="0" x2="1" y2="0">
          <stop offset="0" stop-color="#0a6fb0"/>
          <stop offset="0.6" stop-color="#0492cd"/>
          <stop offset="1" stop-color="#1a7cc0"/>
        </linearGradient>
      </defs>
      <path d="M0 880 C 180 1010, 420 1080, 800 900 L800 1120 L0 1120 Z" fill="url(#waveFill)"/>
      <path d="M0 850 C 190 1000, 440 1060, 800 880 L800 905 C 440 1085, 180 1010, 0 880 Z" fill="url(#bandDeep)"/>
      <path d="M0 905 C 200 1035, 450 1085, 800 925 L800 945 C 450 1105, 200 1050, 0 920 Z" fill="#32a6d7" opacity="0.8"/>
    </svg>
  </section>
</main>
</body>
</html>
```